Data Collection Workbook

We are creating a data gathering booklet that will be completed by our clients (ages 40-90). Due to the volume of information being collected, we are looking for a format that is both inviting to complete and aesthetically pleasing to the eye. The final product will be approximately 20-30 pages, divided into 13 sections. A table of contents, as well as two sample pages are attached.

```html
<!DOCTYPE html>
<html lang="en">
<head>
<meta charset="utf-8">
<title>Contents</title>
<link rel="stylesheet" href="https://fonts.googleapis.com/css2?family=Noto+Sans:wght@400;700&display=swap">
<style>
  :root {
    --mint: #66ffcc;
    --mint-soft: #dafdf1;
    --mint-ring: #d6fcee;
    --violet: #cc66ff;
    --lilac-soft: #f0dafc;
    --lilac-ring: #f1defc;
    --ink: #222222;
    --paper: #ffffff;
  }
  html, body { margin: 0; padding: 0; overflow: hidden; background: var(--paper); }
  .page {
    position: relative;
    width: 849px;
    height: 1200px;
    box-sizing: border-box;
    border: 1px solid #333;
    background: var(--paper);
    font-family: "Noto Sans", Verdana, sans-serif;
    color: var(--ink);
    overflow: hidden;
  }
  .header-band-top { position: absolute; left: 0; top: 0; width: 800px; height: 60px; background: var(--mint); }
  .header-band-bottom { position: absolute; left: 0; top: 133px; width: 800px; height: 12px; background: var(--mint); }
  .header-tab { position: absolute; left: 800px; top: 0; width: 49px; height: 145px; background: var(--violet); }
  .page-title {
    position: absolute; left: 93px; top: 64px; margin: 0;
    font-size: 50px; font-weight: 700; color: var(--violet); line-height: 70px;
  }
  .status-label {
    position: absolute; left: 32px; top: 186px; width: 100px;
    text-align: center; font-size: 17px; line-height: 19px;
  }
  .toc { position: absolute; left: 0; top: 250px; width: 849px; margin: 0; padding: 0; list-style: none; }
  .toc-entry { position: relative; height: 66px; }
  .toc-check {
    position: absolute; left: 60px; top: -5px; width: 32px; height: 32px;
    border-radius: 50%; border: 6px solid var(--mint-ring);
  }
  .toc-bar {
    position: absolute; left: 124px; top: 0; right: 0; height: 32px;
    background: var(--mint-soft);
    display: flex; justify-content: space-between; align-items: center;
    padding: 0 51px 0 13px; box-sizing: border-box;
    font-size: 23.5px;
  }
  .toc-entry:nth-child(even) .toc-check { border-color: var(--lilac-ring); }
  .toc-entry:nth-child(even) .toc-bar { background: var(--lilac-soft); }
  .page-number {
    position: absolute; left: 734px; top: 1085px; width: 79px; height: 78px;
    background: var(--violet); color: var(--paper);
    border-radius: 40px 40px 0 40px;
    display: flex; align-items: center; justify-content: center;
    font-size: 30px;
  }
</style>
</head>
<body>
<div class="page">
  <div class="header-band-top"></div>
  <div class="header-band-bottom"></div>
  <div class="header-tab"></div>
  <h1 class="page-title">Contents</h1>

  <div class="status-label">section<br>complete</div>

  <ol class="toc">
    <li class="toc-entry"><span class="toc-check"></span><div class="toc-bar"><span>My General Information</span><span>3</span></div></li>
    <li class="toc-entry"><span class="toc-check"></span><div class="toc-bar"><span>My Spouse’s General Information; Family Pets</span><span>4</span></div></li>
    <li class="toc-entry"><span class="toc-check"></span><div class="toc-bar"><span>Personal Identification Numbers &amp; Access Codes</span><span>5-6</span></div></li>
    <li class="toc-entry"><span class="toc-check"></span><div class="toc-bar"><span>Doctors &amp; Professional Advisors</span><span>7</span></div></li>
    <li class="toc-entry"><span class="toc-check"></span><div class="toc-bar"><span>Financial Obligations</span><span>9-10</span></div></li>
    <li class="toc-entry"><span class="toc-check"></span><div class="toc-bar"><span>Subscriptions &amp; Social Media</span><span>11</span></div></li>
    <li class="toc-entry"><span class="toc-check"></span><div class="toc-bar"><span>Health Insurance Coverage &amp; Health Information</span><span>13</span></div></li>
    <li class="toc-entry"><span class="toc-check"></span><div class="toc-bar"><span>Insurance Coverage</span><span>15</span></div></li>
    <li class="toc-entry"><span class="toc-check"></span><div class="toc-bar"><span>Important Documents &amp; Other Information</span><span>17</span></div></li>
    <li class="toc-entry"><span class="toc-check"></span><div class="toc-bar"><span>Assets</span><span>19</span></div></li>
    <li class="toc-entry"><span class="toc-check"></span><div class="toc-bar"><span>Source of Income / Retirement Benefits</span><span>21</span></div></li>
    <li class="toc-entry"><span class="toc-check"></span><div class="toc-bar"><span>Monthly Budget in the Event of Incapacity</span><span>23</span></div></li>
  </ol>

  <div class="page-number">2</div>
</div>
</body>
</html>
```